Kentucky residential recovery center needs a flyer design

We need a flyer design for a 16 bed male residential/inpatient recovery center based in Richmond, Kentucky. The facility provides short term (average 30 day) treatment to those struggling with substace abuse and addiction. The design should communicate trust, assurance, safety.
Our wesite provides more information https://morvalcare.org/treatment-services/residential-treatment/

Target Market(s)

Men (typically 30-50) struggling with substance addiction

```html
<!DOCTYPE html>
<html lang="en">
<head>
<meta charset="utf-8">
<title>Morval Care – Residential/Inpatient Treatment Flyer</title>
<link rel="stylesheet" href="https://fonts.googleapis.com/css2?family=Oswald:wght@500;600;700&family=Red+Hat+Display:ital,wght@0,400;0,500;0,700;0,800;0,900;1,800;1,900&display=swap">
<style>
:root{
  --navy:#26287a;
  --navy-deep:#1b1d5e;
  --green:#1f9a45;
  --green-light:#3db458;
  --ink:#1a1a1a;
  --white:#ffffff;
  --canvas:#a9a9a9;
}
*{box-sizing:border-box;margin:0;padding:0}
html,body{width:1200px;height:1117px;overflow:hidden;background:var(--canvas)}
body{position:relative;font-family:"Red Hat Display",sans-serif;color:var(--ink)}
.page{position:absolute;top:165px;width:535px;height:757px;background:var(--white);overflow:hidden}
.page--front{left:56px}
.page--back{left:616px}
.abs{position:absolute}
.photo{position:absolute}

/* front */
.hero-photo{left:0;top:0;width:535px;height:345px;background:linear-gradient(135deg,#c9b48e 0%,#8a7353 35%,#3c3528 65%,#6f5a3f 100%)}
.hero-title{right:32px;top:26px;text-align:right;color:var(--white);font-family:"Oswald",sans-serif;font-weight:700;line-height:1}
.hero-title .kicker{display:block;font-size:29px;letter-spacing:.2px}
.hero-title .main{display:block;font-size:55px;margin-top:2px}
.hero-sub{right:31px;top:114px;text-align:right;color:var(--white);font-size:13.5px;font-weight:700;line-height:1.18}
.brand-seal{border-radius:50%;background:var(--white);display:flex;align-items:center;justify-content:center;text-align:center;color:var(--navy);font-weight:800}
.front-seal{left:349px;top:175px;width:170px;height:170px;font-size:22px;line-height:1.05;border:3px solid var(--navy)}
.thumb{top:345px;height:98px;border-radius:10px;border:3px solid var(--white);background:linear-gradient(160deg,#b9aa8f,#6e6252 60%,#3b3630)}
.client-photo{left:14px;top:432px;width:168px;height:325px;border-radius:70px 70px 0 0;background:linear-gradient(180deg,#9a7b68 0%,#6d6d72 40%,#5b5d63 75%,#c98b86 100%)}
.intro{left:186px;top:456px;width:312px;text-align:center;font-size:10px;line-height:1.12;font-weight:500}
.issues-band{left:143px;top:501px;width:392px;height:177px;background:linear-gradient(120deg,#198c3e,var(--green-light))}
.issues-kicker{left:190px;top:515px;width:330px;text-align:center;color:var(--white);font-size:9px;font-weight:700}
.issues-title{left:190px;top:527px;width:330px;text-align:center;color:var(--white);font-size:17.5px;font-weight:900;white-space:nowrap}
.issue{color:var(--white);font-size:10px;font-weight:700;line-height:1.05;display:flex;align-items:center;gap:8px}
.issue svg{flex:none}
.cta{color:var(--navy);font-weight:900;font-style:italic;text-align:center}
.front-cta{left:200px;top:690px;width:320px;font-size:12px}
.contact{display:flex;align-items:center}
.contact .num{font-family:"Oswald",sans-serif;font-weight:700;color:var(--ink);line-height:1}
.contact .rule{background:#999;width:1px}
.contact .lines{font-weight:700;line-height:1.55}
.contact .lines span{display:flex;align-items:center;gap:4px}
.front-contact{left:203px;top:710px;gap:7px}
.front-contact .num{font-size:27px}
.front-contact .rule{height:26px}
.front-contact .lines{font-size:8.6px}

/* back */
.stages-title{left:40px;top:28px;width:205px;text-align:center;color:var(--navy);font-size:13.5px;font-weight:800;line-height:1.05}
.pill{position:absolute;background:var(--navy);color:var(--white);border-radius:20px;display:flex;align-items:center;justify-content:center;font-weight:800}
.how-pill{left:37px;top:66px;width:208px;height:29px;font-size:15px}
.step{left:41px;display:flex;align-items:center;gap:10px;font-size:8.8px;line-height:1.15}
.step .text{width:172px}
.icon-ring{flex:none;width:40px;height:40px;border-radius:50%;display:flex;align-items:center;justify-content:center}
.icon-ring--green{background:var(--green);box-shadow:0 0 0 3px #d9eedd}
.icon-ring--navy{background:var(--navy);box-shadow:0 0 0 3px #dcdcea;width:36px;height:36px}
.meeting-photo{left:271px;top:17px;width:266px;height:262px;border-radius:50%;border:4px solid var(--white);background:linear-gradient(150deg,#e9e5dc 0%,#cfc8bb 45%,#2c2a2a 70%,#5d4a3a 100%)}
.green-band{left:0;top:464px;width:535px;height:183px;background:linear-gradient(100deg,#168a3b,var(--green) 60%,#249f48)}
.why-shadow{left:31px;top:279px;width:490px;height:263px;border-radius:14px;background:#cfd3cf}
.why-card{left:25px;top:272px;width:486px;height:263px;border-radius:14px;border:2px solid var(--green);background:var(--white)}
.lounge-photo{left:17px;top:299px;width:236px;height:236px;border-radius:50%;border:2px solid var(--navy);box-shadow:inset 0 0 0 8px var(--white);background:linear-gradient(160deg,#ddd6c6 0%,#a89c87 40%,#3d3a36 65%,#6b4f3c 100%)}
.back-seal{left:25px;top:464px;width:106px;height:106px;font-size:14px;line-height:1.05;border:2px solid var(--navy)}
.why-pill{left:276px;top:285px;width:214px;height:26px;font-size:15px}
.stat{left:282px;display:flex;gap:9px;width:240px}
.stat .big{color:var(--green);font-weight:900;font-size:21px;line-height:1}
.stat .tag{color:var(--green);font-weight:800;font-size:8.4px;margin-left:4px}
.stat .desc{font-size:8.3px;line-height:1.15;margin-top:2px}
.stat .head{display:flex;align-items:baseline}
.where{left:0;width:535px;text-align:center;color:var(--white)}
.where-q{top:561px;font-size:18.5px;font-weight:900}
.where-city{top:583px;font-size:18.5px;font-weight:900}
.where-addr{top:606px;font-size:15px;font-weight:500}
.back-cta{left:0;top:664px;width:535px;font-size:17px}
.back-contact{left:40px;top:692px;gap:10px}
.back-contact .num{font-size:38px}
.back-contact .rule{height:32px}
.back-contact .lines{font-size:13px;line-height:1.45}
</style>
</head>
<body>

<section class="page page--front">
  <div class="photo hero-photo" role="img" aria-label="Photo of the residential lounge with leather sofa, coffee table and wall art"></div>
  <svg class="abs" style="left:0;top:0" width="535" height="400" viewBox="0 0 535 400" aria-hidden="true">
    <path d="M188 0 C205 120 330 190 535 192 L535 0 Z" fill="var(--navy)"/>
    <path d="M0 343 L45 343 L45 372 L0 395 Z" fill="var(--navy)"/>
    <path d="M535 343 L495 343 L495 372 L535 355 Z" fill="var(--navy)"/>
    <rect x="0" y="339" width="535" height="8" fill="var(--white)"/>
  </svg>
  <h1 class="abs hero-title"><span class="kicker">RESIDENTIAL/INPATIENT</span><span class="main">TREATMENT</span></h1>
  <p class="abs hero-sub">16 bed male residential/inpatient<br>recovery center based in<br>Richmond, Kentucky.</p>
  <div class="abs brand-seal front-seal">Morval<br>Care</div>

  <div class="photo thumb" style="left:41px;width:147px" role="img" aria-label="Photo of a bedroom with sofa and bunk beds"></div>
  <div class="photo thumb" style="left:195px;width:146px" role="img" aria-label="Photo of a bedroom with bunk beds and green bedding"></div>
  <div class="photo thumb" style="left:348px;width:147px" role="img" aria-label="Photo of a bedroom with dark bedding and bunk beds"></div>

  <div class="abs issues-band"></div>
  <div class="photo client-photo" role="img" aria-label="Photo of a smiling program graduate holding his certificate of completion"></div>

  <p class="abs intro">Inpatient treatment, also referred to as residentialtreatment, provides the highest level of rehab servicesfor patients doagnosed with alcohol, or other drug or substance addiction</p>

  <p class="abs issues-kicker">PROBLEMS WE CAN HELP WITH</p>
  <h2 class="abs issues-title">WHAT ISSUES CAN BE TREATED?</h2>

  <div class="abs issue" style="left:237px;top:558px">
    <svg width="48" height="48" viewBox="0 0 48 48"><circle cx="24" cy="24" r="22" fill="none" stroke="#fff" stroke-width="2.5"/><path d="M24 12 L34 16 V24 C34 30 29 34 24 36 C19 34 14 30 14 24 V16 Z" fill="none" stroke="#fff" stroke-width="2.5"/><line x1="12" y1="12" x2="36" y2="36" stroke="#fff" stroke-width="2.5"/></svg>
    <span>MEDICATION<br>ADDICTION</span></div>
  <div class="abs issue" style="left:370px;top:558px">
    <svg width="48" height="48" viewBox="0 0 48 48"><circle cx="24" cy="24" r="22" fill="none" stroke="#fff" stroke-width="2.5"/><path d="M21 12 H27 V18 L30 22 V36 H18 V22 L21 18 Z" fill="#fff"/><line x1="12" y1="12" x2="36" y2="36" stroke="#fff" stroke-width="2.5"/></svg>
    <span>ALCOHOLISM</span></div>
  <div class="abs issue" style="left:237px;top:617px">
    <svg width="48" height="48" viewBox="0 0 48 48"><circle cx="24" cy="24" r="22" fill="none" stroke="#fff" stroke-width="2.5"/><rect x="13" y="19" width="22" height="10" rx="5" transform="rotate(-40 24 24)" fill="#fff"/><line x1="12" y1="12" x2="36" y2="36" stroke="var(--green)" stroke-width="2.5"/></svg>
    <span>DRUG<br>ADDICTION</span></div>
  <div class="abs issue" style="left:370px;top:617px">
    <svg width="48" height="48" viewBox="0 0 48 48"><circle cx="24" cy="24" r="22" fill="none" stroke="#fff" stroke-width="2.5"/><circle cx="19" cy="20" r="5" fill="#fff"/><circle cx="29" cy="20" r="5" fill="#fff"/><circle cx="24" cy="30" r="5" fill="#fff"/><line x1="12" y1="12" x2="36" y2="36" stroke="#fff" stroke-width="2.5"/></svg>
    <span>BEHAVIORAL<br>HEALTH</span></div>

  <p class="abs cta front-cta">Get in touch with us now. We're here to help!</p>
  <div class="abs contact front-contact">
    <svg width="20" height="20" viewBox="0 0 24 24"><circle cx="12" cy="12" r="10.5" fill="none" stroke="var(--green)" stroke-width="2"/><path d="M8.5 7 L10.5 9.5 L9.3 11 C10 12.7 11.3 14 13 14.7 L14.5 13.5 L17 15.5 L15.8 17 C11.5 16.8 7.2 12.5 7 8.2 Z" fill="var(--green)"/></svg>
    <span class="num">859-555-0142</span>
    <span class="rule"></span>
    <div class="lines">
      <span><svg width="8" height="6" viewBox="0 0 8 6"><rect x=".5" y=".5" width="7" height="5" fill="none" stroke="var(--green)"/><path d="M.5 .5 L4 3.5 L7.5 .5" fill="none" stroke="var(--green)"/></svg>admissions@morvalcare.com</span>
      <span><svg width="8" height="8" viewBox="0 0 8 8"><circle cx="4" cy="4" r="3.5" fill="none" stroke="var(--green)"/><line x1=".5" y1="4" x2="7.5" y2="4" stroke="var(--green)"/></svg>www.morvalcare.org</span>
    </div>
  </div>
</section>

<section class="page page--back">
  <svg class="abs" style="left:0;top:0" width="535" height="90" viewBox="0 0 535 90" aria-hidden="true"><path d="M302 0 L535 0 L535 76 C480 30 390 12 320 25 Z" fill="var(--navy)"/></svg>
  <div class="photo meeting-photo" role="img" aria-label="Photo of the meeting room with an oval table, leather chairs and a small festive tree"></div>

  <h2 class="abs stages-title">STAGES OF RESIDENTIAL<br>RECOVERY PROCESS</h2>
  <div class="pill how-pill">HOW DOES IT WORK?</div>

  <div class="abs step" style="top:106px">
    <span class="icon-ring icon-ring--green"><svg width="20" height="18" viewBox="0 0 20 18"><rect x="1" y="1" width="13" height="9" rx="2" fill="#fff"/><rect x="6" y="7" width="13" height="9" rx="2" fill="none" stroke="#fff" stroke-width="1.5"/></svg></span>
    <span class="text">Speak with our team in private about the nature of your challenges and what you need help with</span></div>
  <div class="abs step" style="top:156px">
    <span class="icon-ring icon-ring--green"><svg width="22" height="16" viewBox="0 0 22 16"><circle cx="11" cy="4" r="3.2" fill="#fff"/><path d="M5 16 C5 10 17 10 17 16 Z" fill="#fff"/><circle cx="4" cy="6" r="2.3" fill="#fff"/><circle cx="18" cy="6" r="2.3" fill="#fff"/></svg></span>
    <span class="text">Together we select an appropriate time slot to book you in for an induction appointment with one of our clinical staff</span></div>
  <div class="abs step" style="top:205px">
    <span class="icon-ring icon-ring--green"><svg width="18" height="16" viewBox="0 0 18 16"><rect x="1" y="1" width="16" height="14" rx="2" fill="none" stroke="#fff" stroke-width="1.6"/><line x1="1" y1="5" x2="17" y2="5" stroke="#fff" stroke-width="1.6"/></svg></span>
    <span class="text">Once the induction is completed, we'll schedule you in to commence your inpatient program</span></div>

  <div class="abs green-band"></div>
  <div class="abs why-shadow"></div>
  <div class="abs why-card"></div>
  <div class="photo lounge-photo" role="img" aria-label="Photo of the common lounge with leather sofas, television and rug"></div>
  <div class="abs brand-seal back-seal">Morval<br>Care</div>

  <div class="pill why-pill">WHY CHOOSE US?</div>

  <div class="abs stat" style="top:328px">
    <span class="icon-ring icon-ring--navy"><svg width="18" height="14" viewBox="0 0 18 14"><path d="M9 1 L17 5 L9 9 L1 5 Z" fill="#fff"/><path d="M4 7 V11 C6 13 12 13 14 11 V7 L9 9.5 Z" fill="#fff"/></svg></span>
    <div><div class="head"><span class="big">100+</span><span class="tag">YEARS</span></div><p class="desc">Over 100 years of medical and clinical<br>experience behind our team</p></div></div>
  <div class="abs stat" style="top:383px">
    <span class="icon-ring icon-ring--navy"><svg width="18" height="16" viewBox="0 0 18 16"><path d="M9 1 L10.5 4.5 L14 5 L11.5 7.3 L12.2 11 L9 9.2 L5.8 11 L6.5 7.3 L4 5 L7.5 4.5 Z" fill="#fff"/></svg></span>
    <div><div class="head"><span class="big">95%</span><span class="tag">SATISFACTION RATING</span></div><p class="desc">Our patients rate us 95 out of 100</p></div></div>
  <div class="abs stat" style="top:429px">
    <span class="icon-ring icon-ring--navy"><svg width="14" height="18" viewBox="0 0 14 18"><circle cx="7" cy="7" r="5.5" fill="none" stroke="#fff" stroke-width="1.8"/><path d="M3 11 L1 17 L5 15 L7 17 L9 15 L13 17 L11 11" fill="#fff"/></svg></span>
    <div><div class="head"><span class="big">#1</span><span class="tag" style="line-height:1.05">BEST DRUG &amp; ALCOHOL<br>REHAB CENTER</span></div><p class="desc">Voted one of the best Alcohol and Drug<br>rehab centers</p></div></div>
  <div class="abs stat" style="top:479px">
    <span class="icon-ring icon-ring--navy"><svg width="18" height="16" viewBox="0 0 18 16"><path d="M9 15 C3 10 1 8 1 5 C1 2 4 0 6 1 C7.5 1.5 8.5 2.5 9 3.5 C9.5 2.5 10.5 1.5 12 1 C14 0 17 2 17 5 C17 8 15 10 9 15 Z" fill="#fff"/></svg></span>
    <div><div class="head"><span class="big">2,500+</span><span class="tag">PATIENTS TREATED</span></div><p class="desc">PATIENTS TREATEDOver 2,500 patients<br>treated successfully and counting</p></div></div>

  <p class="abs where where-q">WHERE ARE WE LOCATED?</p>
  <p class="abs where where-city">RICHMOND, KENTUCKY (MADISON COUNTY)</p>
  <p class="abs where where-addr">1400 &amp;1402 Bramblewood Dr, Richmond, KY 40475</p>

  <p class="abs cta back-cta">Get in touch with us now. We're here to help!</p>
  <div class="abs contact back-contact">
    <svg width="30" height="30" viewBox="0 0 24 24"><circle cx="12" cy="12" r="10.5" fill="none" stroke="var(--green)" stroke-width="2"/><path d="M8.5 7 L10.5 9.5 L9.3 11 C10 12.7 11.3 14 13 14.7 L14.5 13.5 L17 15.5 L15.8 17 C11.5 16.8 7.2 12.5 7 8.2 Z" fill="var(--green)"/></svg>
    <span class="num">859-555-0142</span>
    <span class="rule"></span>
    <div class="lines">
      <span><svg width="12" height="9" viewBox="0 0 8 6"><rect x=".5" y=".5" width="7" height="5" fill="none" stroke="var(--green)" stroke-width=".7"/><path d="M.5 .5 L4 3.5 L7.5 .5" fill="none" stroke="var(--green)" stroke-width=".7"/></svg>admissions@morvalcare.com</span>
      <span><svg width="12" height="12" viewBox="0 0 8 8"><circle cx="4" cy="4" r="3.5" fill="none" stroke="var(--green)" stroke-width=".7"/><line x1=".5" y1="4" x2="7.5" y2="4" stroke="var(--green)" stroke-width=".7"/></svg>www.morvalcare.org</span>
    </div>
  </div>
</section>

</body>
</html>
```